Small boutique Accounting firm needs a tax promotion flyer that stands out

We are an Accounting, taxation and Mortgage Broking firm and looking to promote our services during tax season.
We want to give a new design for our existing flyer on one side. You may consider changing the layout and design, preferably with same content.
Other side, we need a new design to simply communicate that we are Accountants, Tax Agents and Mortgage Brokers too. These three words can be scattered on the page or whatever the way you prefer. You may use our logo and tagline as a background or watermark etc. Feel free to try other colors. At the bottom of this one, we need a disclaimer similar to what we have on our existing flyer.
We may consider using each of these pages on our facebook as a header image or on our website.

Target Market(s)

Individuals and Small businesses

Industry/Entity Type

Accounting

Requirements
Must have
• Please note this is DL size flyer.

```html
<!DOCTYPE html>
<html lang="en">
<head>
<meta charset="utf-8">
<title>Tallow Group – Services Flyer</title>
<link rel="stylesheet" href="https://fonts.googleapis.com/css2?family=Lato:wght@400;700&display=swap">
<style>
  :root {
    --page-bg: #e9e9e9;
    --flyer-green: #6fb53a;
    --watermark-green: #64a634;
    --band-blue: #2b2a86;
    --band-grey: rgba(150, 150, 150, 0.9);
    --band-yellow: #c8bb38;
    --fold-dark: #1b1b1b;
    --icon-green: #6fb53a;
    --white: #ffffff;
    --disclaimer-ink: #333333;
    --footer-white: #f7f7f7;
  }
  html, body {
    margin: 0;
    width: 1200px;
    height: 870px;
    overflow: hidden;
    background: var(--page-bg);
    font-family: "Lato", sans-serif;
  }
  .flyer {
    position: absolute;
    left: 50px;
    top: 176px;
    width: 1100px;
    height: 518px;
    background: var(--flyer-green);
    overflow: hidden;
    box-shadow: 0 6px 18px rgba(0,0,0,0.18);
  }
  .watermark-name {
    position: absolute;
    left: 0;
    top: 24px;
    width: 100%;
    text-align: center;
    font-weight: 400;
    font-size: 64px;
    letter-spacing: 4px;
    color: var(--watermark-green);
    white-space: nowrap;
  }
  .band {
    position: absolute;
    height: 84px;
    display: flex;
    align-items: center;
    box-sizing: border-box;
    padding: 0 24px 0 34px;
    gap: 22px;
  }
  .band-label {
    color: var(--white);
    font-size: 38px;
    font-weight: 400;
    letter-spacing: 0.5px;
    text-transform: uppercase;
    white-space: nowrap;
  }
  .band--accountants { left: 0; top: 290px; width: 400px; background: var(--band-blue); }
  .band--tax { left: 370px; top: 200px; width: 390px; background: var(--band-grey); }
  .band--mortgage { left: 730px; top: 110px; width: 370px; background: var(--band-yellow); }
  .icon-badge {
    width: 66px;
    height: 66px;
    border-radius: 50%;
    background: var(--white);
    flex: none;
    display: flex;
    align-items: center;
    justify-content: center;
  }
  .fold { position: absolute; }
  .fold--tax { left: 370px; top: 284px; }
  .fold--mortgage { left: 730px; top: 194px; }
  .disclaimer {
    position: absolute;
    left: 0;
    bottom: 0;
    width: 100%;
    height: 72px;
    background: var(--footer-white);
    display: flex;
    align-items: center;
    justify-content: center;
    font-size: 17px;
    font-weight: 700;
    color: var(--disclaimer-ink);
  }
</style>
</head>
<body>
  <main class="flyer">
    <div class="watermark-name" aria-hidden="true">TALLOW GROUP</div>

    <div class="band band--accountants">
      <span class="band-label">Accountants</span>
      <span class="icon-badge">
        <svg width="40" height="40" viewBox="0 0 40 40" aria-hidden="true">
          <rect x="8" y="3" width="24" height="34" rx="3" fill="none" stroke="var(--icon-green)" stroke-width="3"/>
          <rect x="12" y="8" width="16" height="8" fill="var(--icon-green)"/>
          <g fill="var(--icon-green)">
            <rect x="12" y="20" width="4" height="3"/><rect x="18" y="20" width="4" height="3"/><rect x="24" y="20" width="4" height="3"/>
            <rect x="12" y="25" width="4" height="3"/><rect x="18" y="25" width="4" height="3"/><rect x="24" y="25" width="4" height="3"/>
            <rect x="12" y="30" width="4" height="3"/><rect x="18" y="30" width="4" height="3"/><rect x="24" y="30" width="4" height="3"/>
          </g>
        </svg>
      </span>
    </div>

    <svg class="fold fold--tax" width="30" height="22" viewBox="0 0 30 22" aria-hidden="true">
      <polygon points="0,0 30,0 30,22" fill="var(--fold-dark)"/>
    </svg>
    <div class="band band--tax">
      <span class="band-label">Tax Agents</span>
      <span class="icon-badge">
        <svg width="44" height="44" viewBox="0 0 44 44" aria-hidden="true">
          <g fill="var(--icon-green)">
            <rect x="12" y="5" width="26" height="4" rx="2"/>
            <rect x="12" y="11" width="26" height="4" rx="2"/>
            <rect x="12" y="17" width="26" height="4" rx="2"/>
            <rect x="12" y="23" width="26" height="4" rx="2"/>
          </g>
          <circle cx="15" cy="30" r="11" fill="var(--icon-green)" stroke="var(--white)" stroke-width="2"/>
          <text x="15" y="35.5" text-anchor="middle" font-family="Lato, sans-serif" font-weight="700" font-size="15" fill="var(--white)">$</text>
        </svg>
      </span>
    </div>

    <svg class="fold fold--mortgage" width="30" height="22" viewBox="0 0 30 22" aria-hidden="true">
      <polygon points="0,0 30,0 30,22" fill="var(--fold-dark)"/>
    </svg>
    <div class="band band--mortgage">
      <span class="band-label">Mortgage</span>
      <span class="icon-badge">
        <svg width="42" height="42" viewBox="0 0 42 42" aria-hidden="true">
          <polygon points="4,21 21,7 38,21" fill="none" stroke="var(--icon-green)" stroke-width="3" stroke-linejoin="round"/>
          <rect x="9" y="20" width="24" height="16" fill="none" stroke="var(--icon-green)" stroke-width="3"/>
          <rect x="18" y="26" width="6" height="10" fill="var(--icon-green)"/>
        </svg>
      </span>
    </div>

    <footer class="disclaimer">
      Tallow Group Pty Ltd (Credit Representative Number 512907) is authorized under Australian Credit Licence Number 406114
    </footer>
  </main>
</body>
</html>
```